Brochure for a website accessibility report

This brochure is related to a report that www.vantrelweb.org sell. The report shows the results of an automated audit of a websites accessibility. It shows details of issues found with screen shots, examples of code and provides remediation advice.

The brochure will be a pdf 8.5 inches by 11 inches. It can be anywhere from 6 to 10 pages.

The GlintMap™ name itself should be “Bree Serif” font. The fonts, styles, colors and sizes are up to you.

The images used and logo of the Office of Digital Reachwork and Q7N logo are upload

We highlighted in blue page extracts from the report we sell. Do not use the blue highlight, it is merely there to show you where the specific examples of the report we sell are vs the other content in the report. The areas in blue which show the content from the actual report should be shown as an extract of the actual page of the report. You have flexibility to change the layout and the way the content look.

The red square callouts over the blue content are callouts that describe the specific page extracts. We used it as a red callout only so that you would be able to see it. You should change the specific location, look and feel of the callout to be appropriate
Updates

Target Market(s)

Marketing and Technical people

Industry/Entity Type

Information Technology

Font styles to use
Sans Serif

Colors

Designer to choose colors to be used in the design.

Requirements
Should not have
• wheelchairs, images of blind people

```html
<!DOCTYPE html>
<html lang="en">
<head>
<meta charset="utf-8">
<title>GlintMap™ Accessibility Report Brochure – Pages 03–04</title>
<link href="https://fonts.googleapis.com/css2?family=Bree+Serif&family=Josefin+Sans:wght@400;600&family=Questrial&family=Roboto+Slab:wght@500&display=swap" rel="stylesheet">
<style>
  :root {
    --backdrop: #d8d9dc;
    --paper: #ffffff;
    --ink: #4a4f57;
    --ink-soft: #7a808a;
    --brand-blue: #1f5ea8;
    --brand-blue-deep: #17467f;
    --night: #141c28;
    --night-mid: #1f2c3d;
    --amber: #6e4b2c;
    --panel: rgba(10, 16, 26, 0.72);
    --line-light: rgba(255, 255, 255, 0.55);
    --white: #ffffff;
  }
  * { box-sizing: border-box; margin: 0; padding: 0; }
  html, body { width: 1200px; height: 900px; overflow: hidden; }
  body {
    background: var(--backdrop);
    font-family: "Questrial", "Helvetica Neue", Arial, sans-serif;
    color: var(--ink);
    position: relative;
  }
  .spread {
    position: absolute;
    left: 44px; top: 90px;
    width: 1112px; height: 720px;
    display: flex;
  }
  .page { position: relative; width: 556px; height: 720px; overflow: hidden; }

  /* ---------- Left page ---------- */
  .page--intro { background: var(--paper); padding: 50px 54px 0 58px; }
  .intro-lead { font-size: 11.5px; line-height: 1.55; color: var(--ink-soft); margin-bottom: 18px; }
  .standards-name {
    text-align: right; margin: 0 40px 18px 0;
    font-family: "Questrial", "Helvetica Neue", Arial, sans-serif;
    font-size: 18px; color: var(--ink); letter-spacing: 0.5px;
  }
  .principles-intro { font-size: 11.5px; line-height: 1.55; margin-bottom: 14px; }
  .principle { margin-bottom: 11px; }
  .principle__title {
    font-family: "Josefin Sans", sans-serif; font-weight: 600;
    font-size: 12px; color: var(--brand-blue); margin-bottom: 3px;
  }
  .principle__text { font-size: 11px; line-height: 1.5; }
  .product-name { font-family: "Bree Serif", serif; color: var(--brand-blue-deep); }
  .closing { font-size: 11.5px; line-height: 1.55; margin-top: 16px; }
  .closing-rule {
    position: absolute; right: 54px; bottom: 62px;
    width: 190px; height: 3px; background: var(--brand-blue);
  }
  .folio {
    position: absolute; bottom: 28px;
    display: flex; align-items: center; gap: 10px;
    font-family: "Josefin Sans", sans-serif; font-size: 10px;
    letter-spacing: 0.8px; text-transform: uppercase;
  }
  .folio--left { left: 58px; color: var(--brand-blue); }
  .folio__number { font-weight: 600; }
  .folio__divider { width: 1px; height: 18px; background: currentColor; }

  /* ---------- Right page ---------- */
  .page--section { color: var(--white); }
  .section-photo {
    position: absolute; inset: 0;
    background:
      radial-gradient(ellipse at 8% 0%, var(--amber) 0%, transparent 45%),
      radial-gradient(ellipse at 80% 75%, #3b4f66 0%, transparent 50%),
      linear-gradient(160deg, var(--night-mid) 0%, var(--night) 60%, #24364a 100%);
  }
  .section-panel {
    position: absolute; left: 40px; right: 36px; top: 40px; height: 450px;
    background: var(--panel); padding: 32px 34px 0 40px;
  }
  .section-title {
    font-family: "Roboto Slab", serif; font-weight: 500;
    font-size: 26px; letter-spacing: 3px; margin-bottom: 14px;
  }
  .section-text { font-size: 11px; line-height: 1.55; color: rgba(255,255,255,0.85); margin-bottom: 8px; }
  .summary-table {
    width: 100%; border-collapse: collapse; margin-top: 12px;
    font-size: 9.5px; color: rgba(255,255,255,0.9);
  }
  .summary-table th, .summary-table td {
    border: 1px solid var(--line-light); padding: 3px 6px; text-align: left;
  }
  .summary-table th { font-family: "Josefin Sans", sans-serif; font-weight: 600; font-size: 10px; }
  .summary-table .count { text-align: center; width: 46px; }
  .summary-table .principle-cell { font-family: "Josefin Sans", sans-serif; font-weight: 600; vertical-align: middle; }
  .slider-bar {
    position: absolute; left: 40px; right: 120px; bottom: 62px;
    height: 2px; background: var(--line-light);
  }
  .slider-bar__knob { position: absolute; left: 0; top: -2px; width: 90px; height: 6px; background: var(--white); }
  .folio--right { right: 40px; color: var(--white); }
</style>
</head>
<body>
  <main class="spread">
    <section class="page page--intro">
      <p class="intro-lead">The Americans with Disabilities Act (ADA) is a comprehensive federal civil rights law prohibiting discrimination on the basis of disability. Its public accommodation rules now reach websites, and courts and regulators routinely cite WCAG 2.1 Level AA as the accepted measure of a website's accessibility.</p>

      <p class="standards-name">Q7N</p>

      <p class="principles-intro">WCAG 2.1 Level AAA consists of 13 guidelines with 78 checkpoints that are organized under four principles:</p>

      <div class="principle">
        <h3 class="principle__title">Principle 1: Perceivable</h3>
        <p class="principle__text">Information and user interface components must be presentable to users in ways they can perceive. Users must be able to perceive the information being presented; it can't be invisible to all of their senses.</p>
      </div>
      <div class="principle">
        <h3 class="principle__title">Principle 2: Operable</h3>
        <p class="principle__text">User interface components and navigation must be operable. The interface cannot require interaction that a user cannot perform.</p>
      </div>
      <div class="principle">
        <h3 class="principle__title">Principle 3: Understandable</h3>
        <p class="principle__text">Information and the operation of a user interface must be understandable. Users must understand the information as well as the operation of the user interface.</p>
      </div>
      <div class="principle">
        <h3 class="principle__title">Principle 4: Robust</h3>
        <p class="principle__text">Content must be robust enough that it can be interpreted reliably by a wide variety of user agents, including assistive technologies. As technologies and user agents evolve, the content should remain accessible.</p>
      </div>

      <p class="closing">Start your journey to a fully compliant website with <span class="product-name">GlintMap™</span>. This detailed compliance and remediation report is generated by scanning your website against hundreds of checkpoints, flagging failures and giving feedback and recommendations on how to fix the problems, based on our years of experience and proven best practices.</p>

      <div class="closing-rule"></div>
      <footer class="folio folio--left">
        <span class="folio__number">03</span>
        <span class="folio__divider"></span>
        <span>Our Mission and Vision</span>
      </footer>
    </section>

    <section class="page page--section">
      <div class="section-photo" role="img" aria-label="Dark blurred photograph of a screen showing lines of website code"></div>

      <div class="section-panel">
        <h2 class="section-title">SECTION 1</h2>
        <p class="section-text">The first section of the report begins with a summary chart that breaks down WCAG 2.1 AAA errors by principle.</p>
        <p class="section-text">Example: WCAG 2.1 AAA summary chart. Each count links to the detailed issue listing in the "Issues Found" section, so you can see exactly where every failure sits on the page.</p>

        <table class="summary-table">
          <thead>
            <tr><th>Principle</th><th>Guideline</th><th class="count">A</th><th class="count">AA</th><th class="count">AAA</th></tr>
          </thead>
          <tbody>
            <tr><td class="principle-cell" rowspan="4">Perceivable</td><td>Guideline 1.1 Text Alternatives</td><td class="count">3</td><td class="count">–</td><td class="count">–</td></tr>
            <tr><td>Guideline 1.2 Time-based Media</td><td class="count">1</td><td class="count">2</td><td class="count">–</td></tr>
            <tr><td>Guideline 1.3 Adaptable</td><td class="count">4</td><td class="count">1</td><td class="count">2</td></tr>
            <tr><td>Guideline 1.4 Distinguishable</td><td class="count">2</td><td class="count">5</td><td class="count">3</td></tr>
            <tr><td class="principle-cell" rowspan="4">Operable</td><td>Guideline 2.1 Keyboard Accessible</td><td class="count">2</td><td class="count">–</td><td class="count">1</td></tr>
            <tr><td>Guideline 2.2 Enough Time</td><td class="count">–</td><td class="count">–</td><td class="count">1</td></tr>
            <tr><td>Guideline 2.3 Seizures</td><td class="count">–</td><td class="count">–</td><td class="count">–</td></tr>
            <tr><td>Guideline 2.4 Navigable</td><td class="count">3</td><td class="count">2</td><td class="count">4</td></tr>
            <tr><td class="principle-cell" rowspan="3">Understandable</td><td>Guideline 3.1 Readable</td><td class="count">1</td><td class="count">–</td><td class="count">2</td></tr>
            <tr><td>Guideline 3.2 Predictable</td><td class="count">–</td><td class="count">1</td><td class="count">–</td></tr>
            <tr><td>Guideline 3.3 Input Assistance</td><td class="count">2</td><td class="count">1</td><td class="count">1</td></tr>
            <tr><td class="principle-cell">Robust</td><td>Guideline 4.1 Compatible</td><td class="count">5</td><td class="count">–</td><td class="count">–</td></tr>
          </tbody>
        </table>
      </div>

      <div class="slider-bar"><span class="slider-bar__knob"></span></div>
      <footer class="folio folio--right">
        <span>Our Mission and Vision</span>
        <span class="folio__divider"></span>
        <span class="folio__number">04</span>
      </footer>
    </section>
  </main>
</body>
</html>
```